Business Card Design

Im electrician in melbourne after a business cards. I have no logos done. I have attached a card that i like but needs to be altered to my business name, so in the picture shows a lead plug into a socket spelling plug, i want the spelling replaced with my company name. I was thinking some thing with a charcoal back ground with yellow or green font.
I have wrote what I'd like above but feel free to try your own ideas and designs.
Industry/Entity Type
Electrician
Contact Information for Business Card
Zul Electrical Services PTY LTD (Display on the front of card, the PTY LTD can be in small font)
REC:58142 (also on the front in small font)
Call Dario (back i dont want my last name on the card)
Phone: 0488157093 (back
Email: zulelectricalservices@kestrelmail.net (back)
Domestic, Commercial, Industrial, (on the back in dot points.)
Look and feel
Each slider illustrates characteristics of the customer's brand and the style your logo design should communicate.

```html
<!DOCTYPE html>
<html lang="en">
<head>
<meta charset="utf-8">
<title>Zul Electrical Services – Business Card</title>
<link rel="stylesheet" href="https://fonts.googleapis.com/css2?family=Open+Sans:wght@400&display=swap">
<style>
  :root {
    --charcoal: #454142;
    --lime: #8dc63f;
    --paper: #ffffff;
    --socket: #ffffff;
  }
  * { margin: 0; padding: 0; box-sizing: border-box; }
  html, body {
    width: 956px;
    height: 1200px;
    overflow: hidden;
    background: var(--paper);
    font-family: "Open Sans", Arial, sans-serif;
  }
  .sheet { position: relative; width: 956px; height: 1200px; }
  .card {
    position: absolute;
    left: 0;
    width: 956px;
    background: var(--charcoal);
  }
  .card--front { top: 0; height: 576px; }
  .card--back { top: 623px; height: 577px; }

  .brand {
    position: absolute;
    left: 156px;
    top: 161px;
    display: flex;
    align-items: center;
    gap: 48px;
  }
  .brand__mark {
    width: 108px;
    height: 107px;
    background: var(--socket);
    border-radius: 12px;
  }
  .brand__name {
    color: var(--lime);
    font-size: 118px;
    font-weight: 400;
    line-height: 1;
    letter-spacing: 1px;
  }

  .company {
    position: absolute;
    left: 0;
    right: 0;
    top: 495px;
    text-align: center;
    color: var(--paper);
    font-size: 32px;
    white-space: nowrap;
  }
  .company__suffix { font-size: 19px; margin-left: 2px; }
  .company__licence { margin-left: 22px; }

  .contact {
    position: absolute;
    left: 0;
    right: 0;
    text-align: center;
    color: var(--lime);
    white-space: nowrap;
  }
  .contact__name { top: 165px; font-size: 56px; }
  .contact__phone { top: 335px; font-size: 36px; }
  .contact__email { top: 388px; font-size: 35px; }

  .services {
    position: absolute;
    left: 0;
    right: 0;
    top: 483px;
    list-style: none;
    display: flex;
    justify-content: center;
    gap: 26px;
    color: var(--lime);
    font-size: 24px;
    white-space: nowrap;
  }
  .services__item::before {
    content: "•";
    margin-right: 9px;
  }
</style>
</head>
<body>
<main class="sheet">
  <section class="card card--front">
    <div class="brand">
      <span class="brand__mark" aria-hidden="true"></span>
      <span class="brand__name">Dario</span>
    </div>
    <p class="company">Zul Electrical Services <span class="company__suffix">PTY LTD</span><span class="company__licence">REC:58142</span></p>
  </section>

  <section class="card card--back">
    <p class="contact contact__name">Dario</p>
    <p class="contact contact__phone">Phone: 0488157093</p>
    <p class="contact contact__email">Email: zulelectricalservices@kestrelmail.net</p>
    <ul class="services">
      <li class="services__item">Domestic</li>
      <li class="services__item">Commercial</li>
      <li class="services__item">Industrial</li>
    </ul>
  </section>
</main>
</body>
</html>
```